Flyer Design

Create a flyer using the logo theme. Single page for to be sent out on email. Attached is an image of the layout, below is the text. A5 and a4 versions.

Simplifying the MAZE

This short workshop is designed as a refresher for those surgeons who have attended a full Cox-MAZE training course, and wish to gain an update on the latest thinking with regards to the surgical treatment of Atrial Fibrillation.
We will start with an overview of the disease burden, talk to the foundation clinical evidence available, and cover the various lesion sets used by surgeons – with a view to simplifying the procedure. The workshop will also explain the technology used, how to treat the Left Atrial Appendage, the best ways to work with your EP colleagues, and involve a short hands-on session to familiarize you with the tools available to perform the Cox-MAZE procedure.

Faculty
{{image}}
Mr. Corwen Halse
Cardiothoracic Surgeon

Mr Halses training was completed at the Brannock Clinic, Rochester, Minnesota, between June 1995 and July 1997 followed by an advanced fellowship with Professor Osric J Talmane at the Westvale General Hospital. Additional expertise required visits to Belgium, Italy, England and the United States. Mr Halse now proctors internationally in order to share his knowledge and further improvement in all areas of minimal access and open cardiac and thoracic surgery.
Further overseas experience at the Westvale General Hospital in Canada culminated in the award of Clinical Fellowship in Cardiovascular Surgery in December 1997.

Mr Halse has contributed to many publications and is referee for Journal articles in very highly regarded professional journals. He performs both Cardiac surgery procedures and thoracic procedures at Harrowgate Private Hospital and Venholt Hospital, Melbourne. Mr Halse has performed in excess of 200 open Maze procedures and 35 via a Thoracoscopic approach.

Venue - TBA
Time : 5pm - 7.30pm, followed by dinner and case presentations

```html
<!DOCTYPE html>
<html lang="en">
<head>
<meta charset="utf-8">
<title>Simplifying the MAZE – Workshop Flyer</title>
<link rel="stylesheet" href="https://fonts.googleapis.com/css2?family=Rubik:wght@700&family=Open+Sans:ital,wght@0,700;1,400;1,600;1,700&family=PT+Serif:ital,wght@0,400;0,700;1,400&family=Fira+Sans+Condensed:ital,wght@1,800&family=Montserrat:wght@500&family=Roboto+Condensed:wght@700&display=swap">
<style>
  :root {
    --navy: #0d3a78;
    --blue: #0a5cab;
    --sky: #12a9e3;
    --orange: #f39220;
    --yellow: #fdd000;
    --teal: #1aa3b0;
    --aqua: #c9eef8;
    --text: #3a3a3a;
    --name-blue: #1c66b0;
    --venue-blue: #133c8c;
  }
  * { margin: 0; padding: 0; box-sizing: border-box; }
  html, body { width: 862px; height: 1200px; overflow: hidden; background: #fff; }
  .flyer { position: relative; width: 862px; height: 1200px; overflow: hidden; background: linear-gradient(180deg, #fff 0%, #f3f3f3 100%); }
  .header-art { position: absolute; left: 0; top: 0; width: 862px; height: 600px; }
  .title {
    position: absolute; top: 66px; left: 0; width: 862px; text-align: center;
    font-family: "Rubik", sans-serif; font-weight: 700; font-size: 60px; color: #fff; letter-spacing: 0.5px;
  }
  .intro {
    position: absolute; top: 170px; left: 110px; width: 642px; text-align: center;
    font-family: "Open Sans", sans-serif; font-style: italic; font-weight: 700; font-size: 18.5px; line-height: 27px; color: #fff;
  }
  .overview {
    position: absolute; top: 430px; left: 140px; width: 582px; text-align: center;
    font-family: "PT Serif", serif; font-size: 12.6px; line-height: 19.2px; color: #2f3a3e;
  }
  .overview .lead { display: block; font-style: italic; font-size: 15.5px; margin-bottom: 3px; }
  .overview b { font-weight: 700; }
  .faculty-heading {
    position: absolute; top: 622px; left: 60px;
    font-family: "Fira Sans Condensed", sans-serif; font-style: italic; font-weight: 800; font-size: 56px; color: var(--orange);
    text-shadow: 1px 2px 2px rgba(0,0,0,0.25);
  }
  .portrait { position: absolute; top: 708px; left: 62px; width: 191px; height: 242px; background: linear-gradient(180deg, #6b6e74 0%, #3c3f45 55%, #1f2126 100%); }
  .speaker-name { position: absolute; top: 958px; left: 40px; width: 240px; text-align: center; font-family: "Montserrat", sans-serif; font-weight: 500; font-size: 21px; color: var(--name-blue); letter-spacing: 0.5px; }
  .speaker-role { position: absolute; top: 986px; left: 40px; width: 240px; text-align: center; font-family: "Open Sans", sans-serif; font-style: italic; font-weight: 600; font-size: 15.5px; color: #222; }
  .divider { position: absolute; left: 306px; top: 640px; width: 1px; height: 364px; background: #c8c8c8; }
  .bio { position: absolute; top: 637px; left: 328px; width: 470px; font-family: "Open Sans", sans-serif; font-style: italic; font-size: 14.2px; line-height: 22px; color: var(--text); text-align: justify; }
  .bio p { margin-bottom: 10px; }
  .brand { position: absolute; top: 1068px; left: 58px; width: 330px; }
  .brand-name { display: flex; align-items: center; gap: 10px; font-family: "Open Sans", sans-serif; font-weight: 700; font-size: 60px; line-height: 1; color: var(--blue); }
  .brand-dot { width: 18px; height: 18px; border-radius: 50%; background: var(--orange); }
  .brand-region { margin-top: 8px; margin-left: 60px; font-family: "Montserrat", sans-serif; font-weight: 500; font-size: 12.5px; color: #555; letter-spacing: 0.5px; }
  .brand-divider { position: absolute; left: 408px; top: 1046px; width: 1px; height: 120px; background: #d5d5d5; }
  .event-details { position: absolute; top: 1042px; left: 440px; font-family: "Roboto Condensed", sans-serif; font-weight: 700; color: var(--venue-blue); }
  .event-details .line { font-size: 35px; line-height: 37px; }
  .event-details .after { margin-top: 8px; font-family: "Open Sans", sans-serif; font-size: 17.5px; color: #444; }
</style>
</head>
<body>
<div class="flyer">
  <svg class="header-art" viewBox="0 0 862 600" aria-hidden="true">
    <defs>
      <linearGradient id="hero" x1="0" y1="0" x2="1" y2="0.4">
        <stop offset="0" stop-color="#0b3d82"/>
        <stop offset="0.55" stop-color="#0a5eae"/>
        <stop offset="1" stop-color="#0db4ea"/>
      </linearGradient>
      <linearGradient id="swoosh" x1="0" y1="1" x2="1" y2="0">
        <stop offset="0" stop-color="#fde000"/>
        <stop offset="0.5" stop-color="#f8a81c"/>
        <stop offset="1" stop-color="#f08a20"/>
      </linearGradient>
      <linearGradient id="bubble" x1="0" y1="0" x2="1" y2="0">
        <stop offset="0" stop-color="#1a9fae"/>
        <stop offset="0.3" stop-color="#c9eef8"/>
        <stop offset="0.7" stop-color="#cdeffa"/>
        <stop offset="1" stop-color="#1aa3b0"/>
      </linearGradient>
    </defs>
    <rect x="14" y="14" width="834" height="400" fill="url(#hero)"/>
    <path d="M14 560 C 120 380, 330 330, 560 370 C 700 395, 790 415, 848 400 L 848 14 L 14 14 Z" fill="url(#hero)"/>
    <path d="M100 340 C 260 290, 430 300, 560 335 C 680 365, 760 390, 848 385" fill="none" stroke="#9cc4e6" stroke-width="10" opacity="0.7"/>
    <path d="M14 560 C 90 420, 250 330, 480 335 C 640 340, 760 420, 848 405 C 760 428, 650 375, 480 348 C 280 330, 120 410, 14 590 Z" fill="url(#swoosh)"/>
    <path d="M124 432 C 300 405, 560 405, 748 432 C 740 520, 620 585, 430 585 C 250 585, 130 520, 124 432 Z" fill="url(#bubble)"/>
  </svg>

  <h1 class="title">Simplifying the MAZE</h1>
  <p class="intro">This SHORT WORKSHOP is designed as a refresher for those surgeons who have attended a full Cox-MAZE training course, and wish to gain an update on the latest thinking with regards to the surgical treatment of Atrial Fibrillation.</p>

  <p class="overview"><span class="lead">We will start with an</span>overview of the <b>disease burden</b>, talk to the <b>foundation clinical evidence available</b>,<br>and cover the <b>various lesion sets used by surgeons</b> – with a view to simplifying the procedure.<br>The workshop will also <b>explain the technology used</b>, <b>how to treat the Left Atrial Appendage</b>,<br>the <b>best ways to work with your EP colleagues</b>, and involve a short hands-on<br>session to familiarize you with the tools available to<br>perform the Cox-MAZE procedure.</p>

  <h2 class="faculty-heading">Faculty</h2>
  <div class="portrait" role="img" aria-label="Portrait photograph of Mr. Corwen Halse, cardiothoracic surgeon"></div>
  <p class="speaker-name">MR. CORWEN HALSE</p>
  <p class="speaker-role">Cardiothoracic Surgeon</p>
  <div class="divider"></div>

  <div class="bio">
    <p>Mr Halses training was completed at the Brannock Clinic, Rochester, Minnesota, between June 1995 and July 1997 followed by an advanced fellowship with Professor Osric J Talmane at the Westvale General Hospital. Additional expertise required visits to Belgium, Italy, England and the United States. Mr Halse now proctors internationally in order to share his knowledge and further improvement in all areas of minimal access and open cardiac and thoracic surgery.</p>
    <p>Further overseas experience at the Westvale General Hospital in Canada culminated in the award of Clinical Fellowship in Cardiovascular Surgery in December 1997.</p>
    <p>Mr Halse has contributed to many publications and is referee for Journal articles in very highly regarded professional journals. He performs both Cardiac surgery procedures and thoracic procedures at Harrowgate Private Hospital and Venholt Hospital, Melbourne. Mr Halse has performed in excess of 200 open Maze procedures and 35 via a Thoracoscopic approach.</p>
  </div>

  <div class="brand">
    <div class="brand-name">Veltria<span class="brand-dot"></span></div>
    <div class="brand-region">AUSTRALIA AND NEW ZEALAND</div>
  </div>
  <div class="brand-divider"></div>

  <div class="event-details">
    <div class="line">VENUE:&nbsp; TBA</div>
    <div class="line">TIME: 5PM-7.30PM</div>
    <div class="after">Followed By Dinner And Case Presentations</div>
  </div>
</div>
</body>
</html>
```